Business Card Design Project

looking for a stylish and simple double sided business card.
I am an artist - specialising in fashion illustration, portraits and murals.
the front should be simply my name and tag:

D U R E S K
Living in colour

My preference is for a Black background with DURESK in red or embossed.
Living in colour in White or multi-coloured.

the back will have detail:

Personalised Art
Portraits, Murals, Fashion Illustration

0437 582 190
duresk@duresk.com.au
www.duresk.com.au

Target Market(s)

Adults that are based in western speaking countries who have an appreciation for art and design. Portraits and wall art
Business owners who may need personalised all art for their business space. Murals and personalised canvass.
People in the fashion industry, who may require fashion illustrations.

Industry/Entity Type

Fashion

Requirements
Must have
• BOLD but simple at the same time, timeless modern element to it.
Nice to have
• simple lettering
Should not have
• Not too busy or wordy,

```html
<!DOCTYPE html>
<html lang="en">
<head>
<meta charset="utf-8">
<title>Duresk — Business Card Back</title>
<link rel="stylesheet" href="https://fonts.googleapis.com/css2?family=Roboto:wght@300&display=swap">
<style>
  :root {
    --card-black: #000000;
    --ink-white: #ffffff;
    --accent-red: #e8141b;
    --stripe-red: #ff0000;
  }
  html, body {
    margin: 0;
    padding: 0;
    width: 1200px;
    height: 720px;
    overflow: hidden;
    background: var(--card-black);
  }
  .card-back {
    position: relative;
    width: 1200px;
    height: 720px;
    background: var(--card-black);
    color: var(--ink-white);
    font-family: "Roboto", "Helvetica Neue", Arial, sans-serif;
    font-weight: 300;
  }
  .accent-stripe {
    position: absolute;
    left: 0;
    top: 98px;
    width: 952px;
    height: 12px;
  }
  .services {
    position: absolute;
    left: 0;
    right: 0;
    top: 248px;
    margin: 0;
    padding: 0;
    list-style: none;
    text-align: center;
    font-size: 45px;
    letter-spacing: 1.5px;
    line-height: 58px;
  }
  .services .highlight {
    color: var(--accent-red);
  }
  .contact {
    position: absolute;
    left: 26px;
    right: 26px;
    top: 656px;
    display: flex;
    justify-content: space-between;
    font-size: 35px;
    letter-spacing: 0.5px;
  }
  .contact .phone {
    letter-spacing: 4px;
  }
</style>
</head>
<body>
  <main class="card-back">
    <svg class="accent-stripe" viewBox="0 0 952 12" preserveAspectRatio="none" aria-hidden="true">
      <defs>
        <linearGradient id="stripe-fade" x1="0" y1="0" x2="1" y2="0">
          <stop offset="0" stop-color="#ff0000"/>
          <stop offset="0.2" stop-color="#ff2020"/>
          <stop offset="0.42" stop-color="#ffb0b0"/>
          <stop offset="0.6" stop-color="#ffffff"/>
          <stop offset="0.72" stop-color="#d8e6e6"/>
          <stop offset="0.86" stop-color="#556060"/>
          <stop offset="1" stop-color="#000000"/>
        </linearGradient>
      </defs>
      <rect x="0" y="0" width="952" height="12" fill="url(#stripe-fade)"/>
    </svg>

    <ul class="services">
      <li>PERSONALISED&nbsp; <span class="highlight">ART</span></li>
      <li>PORTRAITS</li>
      <li>MURALS</li>
      <li>FASHION&nbsp; <span class="highlight">ILLUSTRATION</span></li>
    </ul>

    <footer class="contact">
      <span class="web">www.duresk.com.au</span>
      <span class="phone">0437 582 190</span>
      <span class="email">duresk@duresk.com.au</span>
    </footer>
  </main>
</body>
</html>
```